40k Ultra High Pressure Waterblasting Ad

Clean, Simple, To the point. We need an ad for our industry magazine. Our company Brightwell Spraytek Systems, Inc. caters to contractors in the Utra High Pressure Waterblasting Industry. We manufacture in house a majority of the items we sell. We'd like the ad to imply that we believe in good customer service, building relationships with our customers and going above and beyond to meet our customer needs. Our main products we sell are our Quillstone Nozzles and Dorvane Mellick Hoses. Our website is Brightwellspraytek.example for images of our products.

Attached are some of our previous ads we've made.

I like the icons we used in the "Dorvane ad" listing some of our keys products we sell.

Target Market(s)

Contractors

Industry/Entity Type

Industry

Colors

Designer to choose colors to be used in the design.

Requirements
Must have
• At least 1 item we sell

```html
<!DOCTYPE html>
<html lang="en">
<head>
<meta charset="utf-8">
<title>Brightwell Spraytek Systems – UHP Essentials Ad</title>
<link rel="stylesheet" href="https://fonts.googleapis.com/css2?family=Oswald:wght@500;600;700&family=Montserrat:wght@500;600;700&display=swap">
<style>
  :root {
    --navy: #1d2466;
    --navy-deep: #141a52;
    --sky: #3d8fd6;
    --ice: #dbeaf7;
    --paper: #ffffff;
    --mist: #e4e6ea;
    --mist-dark: #c9ccd3;
    --bronze: #8b6a4f;
    --stage: #eceef1;
    --ink-white: #ffffff;
  }
  * { box-sizing: border-box; margin: 0; padding: 0; }
  html, body { width: 1200px; height: 848px; overflow: hidden; }
  body { background: var(--stage); font-family: "Montserrat", sans-serif; position: relative; }

  .ad {
    position: absolute; left: 300px; top: 0;
    width: 600px; height: 848px;
    background: var(--paper);
    overflow: hidden;
    box-shadow: 0 6px 24px rgba(0,0,0,.18);
  }

  /* product icon band */
  .product-band {
    position: absolute; left: 0; top: 0; width: 600px; height: 118px;
    background: var(--navy);
    display: flex; justify-content: space-around; align-items: center;
    padding: 0 14px;
  }
  .product { display: flex; flex-direction: column; align-items: center; width: 104px; color: var(--ink-white); }
  .product svg { width: 46px; height: 40px; margin-bottom: 8px; }
  .product-name { font-size: 10.5px; font-weight: 600; text-align: center; line-height: 1.25; }

  /* product photo area */
  .hose-photo {
    position: absolute; left: 40px; top: 138px; width: 250px; height: 150px;
    border-radius: 50%;
    background: radial-gradient(ellipse at center, var(--paper) 28%, #a9adb3 32%, #7d8288 52%, #b8bcc1 70%, var(--paper) 72%);
  }
  .fittings-photo {
    position: absolute; left: 40px; top: 300px; width: 290px; height: 70px;
    border-radius: 14px;
    background: linear-gradient(90deg, #6e5744, var(--bronze), #b79a80, var(--bronze), #5f4a39);
  }
  .brand-mark {
    position: absolute; left: 350px; top: 230px; width: 230px;
    display: flex; align-items: center; gap: 10px;
  }
  .brand-mark .dot { width: 18px; height: 18px; border-radius: 50%; background: var(--sky); flex: none; }
  .brand-name {
    font-family: "Oswald", sans-serif; font-weight: 700; font-size: 30px;
    line-height: 1; color: var(--navy); text-transform: uppercase;
  }
  .spray {
    position: absolute; left: 440px; top: 330px; width: 160px; height: 34px;
    background: linear-gradient(90deg, var(--sky), var(--ice) 60%, rgba(255,255,255,0));
    border-radius: 0 40px 40px 0;
  }

  /* info panel */
  .info-panel {
    position: absolute; left: 0; top: 395px; width: 600px; height: 453px;
    background: linear-gradient(160deg, #f4f5f7 0%, var(--mist) 55%, var(--mist-dark) 100%);
  }
  .headline {
    position: absolute; left: 0; top: 22px; width: 600px;
    font-family: "Oswald", sans-serif; font-weight: 700;
    font-size: 30px; line-height: 1.12; color: var(--navy);
    text-transform: uppercase; text-align: center;
  }
  .headline span { display: block; white-space: nowrap; }
  .price-pill {
    position: absolute; left: 100px; top: 104px; width: 400px; height: 42px;
    border-radius: 21px; background: var(--navy); color: var(--ink-white);
    font-family: "Oswald", sans-serif; font-weight: 500; font-size: 22px;
    letter-spacing: 1px; text-transform: uppercase;
    display: flex; align-items: center; justify-content: center;
  }
  .offer-list {
    position: absolute; left: 36px; top: 176px; width: 335px;
    list-style: none; color: var(--navy-deep);
    font-size: 14px; font-weight: 500; line-height: 1.6;
  }
  .offer-list li { white-space: nowrap; }
  .offer-list li::before {
    content: ""; display: inline-block; width: 7px; height: 7px;
    border-radius: 50%; background: var(--navy); margin-right: 9px; vertical-align: 2px;
  }
  .jetlance-photo {
    position: absolute; left: 380px; top: 168px; width: 190px; height: 164px;
    border-radius: 10px;
    background: linear-gradient(135deg, #d7d9dd, #a8acb2 50%, #3b3e44);
  }
  .partner-name {
    position: absolute; left: 430px; top: 340px;
    font-family: "Oswald", sans-serif; font-weight: 700; font-size: 24px; line-height: 1;
    color: var(--sky); text-transform: uppercase;
  }
  .contact-line {
    position: absolute; left: 0; top: 398px; width: 600px;
    border-top: 2px solid var(--navy); padding-top: 14px;
    font-family: "Oswald", sans-serif; font-weight: 600; font-size: 11.5px;
    color: var(--navy); text-align: center; text-transform: uppercase;
    white-space: nowrap;
  }
  .contact-line .sep { margin: 0 7px; }
</style>
</head>
<body>
  <article class="ad">
    <header class="product-band">
      <div class="product">
        <svg viewBox="0 0 46 40"><g fill="#fff"><circle cx="12" cy="24" r="7"/><circle cx="23" cy="16" r="7"/><circle cx="34" cy="24" r="7"/></g><g fill="#1d2466"><circle cx="12" cy="24" r="3"/><circle cx="23" cy="16" r="3"/><circle cx="34" cy="24" r="3"/></g></svg>
        <span class="product-name">Pump Replacement Parts</span>
      </div>
      <div class="product">
        <svg viewBox="0 0 46 40"><path d="M6 16h20l8 4-8 4H6z" fill="#fff"/><path d="M36 20h8" stroke="#fff" stroke-width="2"/></svg>
        <span class="product-name">Quillstone Nozzles</span>
      </div>
      <div class="product">
        <svg viewBox="0 0 46 40" fill="#fff"><rect x="4" y="10" width="38" height="6"/><rect x="10" y="16" width="5" height="18"/><rect x="30" y="16" width="5" height="18"/></svg>
        <span class="product-name">Pneumatic Rotating Jetlance</span>
      </div>
      <div class="product">
        <svg viewBox="0 0 46 40" fill="#fff"><rect x="17" y="4" width="12" height="10"/><rect x="13" y="14" width="20" height="14"/><rect x="17" y="28" width="12" height="8"/></svg>
        <span class="product-name">Fittings and Adapters</span>
      </div>
      <div class="product">
        <svg viewBox="0 0 46 40"><circle cx="23" cy="20" r="15" fill="#fff"/></svg>
        <span class="product-name">Safety Gear</span>
      </div>
    </header>

    <div class="hose-photo" role="img" aria-label="Coiled grey ultra high pressure hose"></div>
    <div class="fittings-photo" role="img" aria-label="Row of bronze threaded fittings"></div>
    <div class="brand-mark">
      <span class="dot"></span>
      <span class="brand-name">Brightwell Spraytek</span>
    </div>
    <div class="spray" role="img" aria-label="Water jet spray"></div>

    <section class="info-panel">
      <h1 class="headline"><span>Supplying the essentials in the</span><span>UHP surface preparation industry</span></h1>
      <div class="price-pill">At affordable prices</div>
      <ul class="offer-list">
        <li>Couplers And Fittings</li>
        <li>Pneumatically Driven Rotating Jetlance</li>
        <li>Numerous Types Of Heat Treated</li>
        <li>Quillstone Nozzles &amp; Tips</li>
        <li>Variety Of Pump Replacement Parts</li>
        <li>Distributor Of Dorvane Mellick Hoses</li>
      </ul>
      <div class="jetlance-photo" role="img" aria-label="Pneumatic rotating jetlance tool"></div>
      <div class="partner-name">Dorvane</div>
      <p class="contact-line">Email: info@brightwellspraytek.example<span class="sep">|</span>Phone: 555-014-2290<span class="sep">|</span>www.brightwellspraytek.example</p>
    </section>
  </article>
</body>
</html>
```